a4 size poster for theatre school

I am looking for an eye catching poster for my theatre school - Bright Lantern Stage school - View our website here for the style we have already www.brightlanternstage.co.uk

Wording needs to include;

* Award Winning, Accredited, Affordable Performing Arts Classes taught by Leading Industry Experts

* Ages 4- 21 years

* All classes contain all three disciplines of Drama, Singing & Dance keeping cost low and enjoyment high

* Classes offered;
Drama
QWERN
Singing
PBSO dance
Freestyle Ballet
Freestyle Tap
Contemporary
Street
Jazz Musical Theatre

* FREE casting agency for TV and Theatre Available. Ten pupils currently performing in West End Productions, 8 pupils currently on screen in TV commercials, several pupils currently working on film & TV projects for Zentrovia, Velmora Plus & Kestrel TV.

* Optional PBSO and QWERN exams

* Unparalleled performance opportunities both locally and in the West End

Our quality training is evident in our pupils success

* Now in our successful 17th Year!

* Awarded recognition from the Board for Youth Stagecraft and Movement Studies - The industry regulator for children's performing arts training.

Target Market(s)

Parents & Children ages 4-21 years

Industry/Entity Type

Performing arts

Font styles to use
Other font styles liked:
• Arvo

Colors
EB3D1F
EC4F4E
F09395
F8D3D4
FCEDEE
6B429C
8869AF
B7A5CE
E3DAEB
F3F0F8

Requirements
Must have
• A good mix of photo's pf boys & girls. Different ethnicities. Different ages
Nice to have
• Wording very clear
Should not have
• Too many words

```html
<!DOCTYPE html>
<html lang="en">
<head>
<meta charset="utf-8">
<title>Bright Lantern Stage School – Poster</title>
<link rel="stylesheet" href="https://fonts.googleapis.com/css2?family=Arvo:wght@400;700&family=Open+Sans:wght@400;600;700&family=Oswald:wght@600&display=swap">
<style>
  :root{
    --red:#EB3D1F;
    --red-bright:#E5212C;
    --red-deep:#B5202A;
    --pink:#F09395;
    --purple:#6B429C;
    --purple-mid:#8869AF;
    --lavender:#B7A5CE;
    --lavender-light:#E3DAEB;
    --ink:#2B1E5C;
    --text:#3A3050;
    --yellow:#FFEE33;
    --cream:#FDF3BE;
    --stage:#E9ECF4;
    --white:#FFFFFF;
  }
  *{box-sizing:border-box;margin:0;padding:0}
  html,body{width:1200px;height:1200px;overflow:hidden;background:var(--stage)}
  .canvas{position:relative;width:1200px;height:1200px;background:var(--stage)}
  .poster{position:absolute;left:204px;top:40px;width:792px;height:1120px;background:var(--white);overflow:hidden;box-shadow:0 4px 14px rgba(40,40,80,.18)}
  .poster-shapes{position:absolute;inset:0}
  .abs{position:absolute}

  .age-band{left:12px;top:366px;transform:rotate(-14.5deg);transform-origin:left center;font-family:'Oswald',sans-serif;font-weight:600;font-size:32px;color:var(--yellow);letter-spacing:.5px;white-space:nowrap}

  .school-name{left:283px;top:262px;width:200px;text-align:center;font-family:'Arvo',serif;font-weight:700;font-size:25px;line-height:1.15;color:var(--red-bright)}

  .promise-list{left:548px;top:272px;list-style:none}
  .promise-list li{display:flex;align-items:flex-start;gap:9px;font-family:'Arvo',serif;font-weight:700;font-size:24px;line-height:28px;color:var(--ink);margin-bottom:3px}
  .promise-list svg{flex:none;margin-top:2px}

  .headline{left:250px;top:444px;width:530px;text-align:center;font-family:'Arvo',serif;color:var(--purple)}
  .headline .lead{font-weight:700;font-size:22px;line-height:26px}
  .headline .sub{font-weight:400;font-size:22px;line-height:28px}
  .headline .rule{height:0;border-top:3px dotted var(--red-bright);margin:3px 6px 5px}
  .headline .tagline{font-weight:700;font-size:14.5px;color:var(--red-deep);letter-spacing:.2px}

  .casting-box{left:295px;top:546px;width:468px;height:137px;background:var(--cream);border:1.5px dashed var(--red-bright);border-radius:9px;padding:10px 22px 0 30px}
  .casting-box ul{list-style:none}
  .casting-box li{position:relative;font-family:'Open Sans',sans-serif;font-size:13.4px;line-height:16.2px;color:var(--text)}
  .casting-box li::before{content:"•";position:absolute;left:-11px;color:var(--red-bright)}
  .casting-box strong{color:var(--red-bright);font-weight:700}

  .accreditation{left:312px;top:704px;display:flex;align-items:center}
  .accreditation .badge{width:120px;height:26px}
  .accreditation p{margin-left:10px;padding-left:8px;border-left:2px solid var(--red-bright);width:330px;font-family:'Open Sans',sans-serif;font-weight:600;font-size:12.8px;line-height:15.5px;color:var(--ink)}

  .classes{left:28px;top:480px;width:260px}
  .classes h2{font-family:'Arvo',serif;font-weight:700;font-size:27px;line-height:32px;color:var(--lavender);-webkit-text-stroke:1.2px var(--white);text-shadow:1px 1px 0 var(--purple);letter-spacing:.5px}
  .class-list{list-style:none;margin-top:14px;padding-left:5px}
  .class-list li{position:relative;padding-left:17px;font-family:'Open Sans',sans-serif;font-weight:600;font-size:16px;line-height:20.7px;color:var(--ink);letter-spacing:.6px;text-transform:uppercase}
  .class-list li::before{content:"★";position:absolute;left:0;top:0;font-size:11px;color:var(--red-bright)}
  .classes .note{margin-top:10px;font-family:'Open Sans',sans-serif;font-size:13.6px;line-height:17.5px;color:var(--text);width:230px}

  .exam-band{left:10px;top:930px;transform:rotate(-16.5deg);transform-origin:left center;font-family:'Arvo',serif;font-weight:700;font-size:16.5px;color:var(--white);white-space:nowrap}

  .anniversary{left:312px;top:878px;transform:rotate(-11.7deg);transform-origin:left center;white-space:nowrap;font-family:'Arvo',serif;font-weight:700;color:var(--white);font-size:17.5px}
  .anniversary .year{color:var(--yellow);font-size:37px;margin-left:8px;vertical-align:-2px}

  .website{right:14px;top:1080px;font-family:'Arvo',serif;font-weight:700;font-size:14px;color:var(--ink);letter-spacing:.2px;white-space:nowrap}
</style>
</head>
<body>
<main class="canvas">
  <article class="poster">
    <svg class="poster-shapes" width="792" height="1120" viewBox="0 0 792 1120">
      <defs>
        <linearGradient id="photoDance" x1="0" y1="0" x2="1" y2="1">
          <stop offset="0" stop-color="#2B3AA6"/><stop offset="1" stop-color="#6F54B8"/>
        </linearGradient>
        <linearGradient id="photoCostume" x1="0" y1="0" x2="1" y2="1">
          <stop offset="0" stop-color="#B9A8E0"/><stop offset="1" stop-color="#8E6B7A"/>
        </linearGradient>
        <linearGradient id="photoMakeup" x1="0" y1="0" x2="1" y2="1">
          <stop offset="0" stop-color="#E0D6EA"/><stop offset="1" stop-color="#7A4B2A"/>
        </linearGradient>
        <linearGradient id="photoShow" x1="0" y1="0" x2="1" y2="1">
          <stop offset="0" stop-color="#17161E"/><stop offset="1" stop-color="#5A4E66"/>
        </linearGradient>
        <radialGradient id="logoDisc" cx=".45" cy=".4" r=".65">
          <stop offset="0" stop-color="#FFFFFF"/><stop offset="1" stop-color="#B7A5CE"/>
        </radialGradient>
      </defs>

      <polygon role="img" aria-label="Photo: costumed young performers in a musical" fill="url(#photoCostume)" points="360,0 792,0 792,190 470,262 330,240"/>
      <polygon role="img" aria-label="Photo: teenage dancers performing on a blue-lit stage" fill="url(#photoDance)" points="0,0 400,0 300,300 201,323 0,375"/>

      <polygon class="age-banner" fill="var(--red-bright)" points="0,375 201,323 201,388 0,441"/>
      <polygon class="classes-panel" fill="var(--lavender)" points="0,441 201,388 290,823 0,910"/>
      <polygon class="exam-banner" fill="var(--purple-mid)" points="0,910 293,823 307,864 0,952"/>
      <polygon role="img" aria-label="Photo: two children in animal stage make-up and costumes" fill="url(#photoMakeup)" points="0,952 307,864 322,1110 0,1110"/>

      <polygon class="anniversary-banner" fill="var(--red-bright)" points="301,851 792,749 792,802 310,903"/>
      <line x1="560" y1="852" x2="792" y2="805" stroke="#FFFFFF" stroke-width="2.5" stroke-dasharray="2 4"/>
      <polygon role="img" aria-label="Photo: full cast performing a dance number on stage" fill="url(#photoShow)" points="310,903 792,802 792,960 470,1056 470,1110 322,1110"/>
      <polygon class="accent-strip" fill="var(--lavender)" points="470,1056 792,960 792,992 485,1068"/>

      <rect class="base-stripe" x="0" y="1108" width="792" height="12" fill="var(--red-bright)"/>

      <g class="globe-icon" transform="translate(752,1043)">
        <circle r="22" fill="var(--red-bright)"/>
        <circle r="13" fill="none" stroke="#FFFFFF" stroke-width="2.2"/>
        <ellipse rx="5.5" ry="13" fill="none" stroke="#FFFFFF" stroke-width="2"/>
        <line x1="-13" y1="0" x2="13" y2="0" stroke="#FFFFFF" stroke-width="2"/>
      </g>

      <path class="logo-arc" d="M 305 172 A 140 140 0 0 0 330 420" fill="none" stroke="var(--red-bright)" stroke-width="3"/>
      <circle class="logo-disc" cx="383" cy="295" r="124" fill="url(#logoDisc)" stroke="var(--red-bright)" stroke-width="3"/>
    </svg>

    <div class="abs age-band">4- 21 YEARS</div>

    <div class="abs school-name">Bright Lantern Stage School</div>

    <ul class="abs promise-list">
      <li><svg width="24" height="24" viewBox="0 0 24 24"><circle cx="12" cy="12" r="11" fill="var(--red)"/><path d="M6 12l4 4 8-9" fill="none" stroke="#FFD23F" stroke-width="3" stroke-linecap="round" stroke-linejoin="round"/></svg><span>AWARD<br>WINNING</span></li>
      <li><svg width="24" height="24" viewBox="0 0 24 24"><circle cx="12" cy="12" r="11" fill="var(--red)"/><path d="M6 12l4 4 8-9" fill="none" stroke="#FFD23F" stroke-width="3" stroke-linecap="round" stroke-linejoin="round"/></svg><span>ACCREDITED</span></li>
      <li><svg width="24" height="24" viewBox="0 0 24 24"><circle cx="12" cy="12" r="11" fill="var(--red)"/><path d="M6 12l4 4 8-9" fill="none" stroke="#FFD23F" stroke-width="3" stroke-linecap="round" stroke-linejoin="round"/></svg><span>AFFORDABLE</span></li>
    </ul>

    <header class="abs headline">
      <h1 class="lead">PERFORMING ARTS CLASSES</h1>
      <p class="sub">TAUGHT BY LEADING INDUSTRY EXPERTS</p>
      <div class="rule"></div>
      <p class="tagline">OUR QUALITY TRAINING IS EVIDENT IN OUR PUPILS SUCCESS</p>
    </header>

    <section class="abs casting-box">
      <ul>
        <li><strong>FREE casting agency</strong> for TV and Theatre Available.</li>
        <li>10 pupils currently performing in West End Productions, 8 pupils currently on screen in TV commercials, several pupils currently working on film &amp; TV projects for Zentrovia, Velmora Plus &amp; Kestrel TV.</li>
        <li>Unparalleled performance opportunities both locally and in the West End</li>
      </ul>
    </section>

    <section class="abs accreditation">
      <svg class="badge" viewBox="0 0 120 26" role="img" aria-label="Accreditation badge">
        <rect width="120" height="26" fill="#FFFFFF" stroke="#2B2B2B" stroke-width="1"/>
        <rect x="34" y="0" width="86" height="20" fill="#1EA3DC"/>
      </svg>
      <p>Awarded recognition from the Board for Youth Stagecraft and Movement Studies - The industry regulator for children's performing arts training.</p>
    </section>

    <section class="abs classes">
      <h2>CLASSES<br>OFFERED:</h2>
      <ul class="class-list">
        <li>Drama</li>
        <li>QWERN</li>
        <li>Singing</li>
        <li>PBSO Dance</li>
        <li>Freestyle Ballet</li>
        <li>Freestyle Tap</li>
        <li>Contemporary</li>
        <li>Street</li>
        <li>Jazz Musical<br>Theatre</li>
      </ul>
      <p class="note">All classes contain all 3 disciplines of Drama, Singing &amp; Dance keeping cost low and enjoyment high!</p>
    </section>

    <div class="abs exam-band">Optional PBSO &amp; QWERN exams</div>

    <div class="abs anniversary">NOW IN OUR SUCCESSFUL <span class="year">17th Year!</span></div>

    <div class="abs website">WWW.BRIGHTLANTERNSTAGE.CO.UK</div>
  </article>
</main>
</body>
</html>
```